Tavenlume: Smart Quotes for Wine Lovers

Hello. I am completing book of quotes for wine lovers. Need the text formatted so that it is easy to read and aesthetically pleasing...modern, clean, smart. Number the pages. The cover is complete. Book is small square. 7.5 by 7.5 inches. If you want to show me first few pages that would be awesome. Thank you!
Updates

I edited the quotes so if you downloaded first ones, please grab these ones instead, thank you! 

Target Market(s)

wine lovers. Urban. Modern.

Industry/Entity Type

Quotes

Requirements
Should not have
• No color. black and white only.

```html
<!DOCTYPE html>
<html lang="en">
<head>
<meta charset="utf-8">
<title>Tavenlume – Smart Quotes for Wine Lovers</title>
<link rel="stylesheet" href="https://fonts.googleapis.com/css2?family=Libre+Bodoni:wght@400;700&display=swap">
<style>
  :root {
    --backdrop: #e6e6e6;
    --paper: #ffffff;
    --ink: #111111;
    --rule: #222222;
    --marker-top: #ececec;
    --marker-bottom: #bdbdbd;
  }
  * { margin: 0; padding: 0; box-sizing: border-box; }
  html, body {
    width: 1200px; height: 900px; overflow: hidden;
    background: var(--backdrop);
    font-family: "Libre Bodoni", "Times New Roman", serif;
    color: var(--ink);
  }
  .spread {
    position: absolute; left: 55px; top: 180px;
    width: 1080px; height: 540px;
    display: flex;
    background: var(--paper);
    border: 1px solid var(--rule);
    box-shadow: 1px 2px 0 var(--rule);
  }
  .page { position: relative; width: 540px; height: 100%; }
  .page + .page { border-left: 1px solid var(--rule); }
  .page-marker {
    position: absolute; top: 0; width: 44px; height: 112px;
    background: linear-gradient(180deg, var(--marker-top), var(--marker-bottom));
  }
  .page--left .page-marker { left: 16px; }
  .page--right .page-marker { right: 16px; }
  .page-number {
    position: absolute; top: 62px; width: 44px;
    text-align: center;
    font-weight: 700; font-size: 12px; line-height: 16px;
  }
  .page--left .page-number { left: 16px; }
  .page--right .page-number { right: 16px; }
  .quote {
    position: absolute; top: 292px; left: 0; right: 0;
    top: 112px;
    text-align: center;
    font-weight: 700; font-size: 29px; line-height: 38.5px;
  }
  .author-note {
    position: absolute; left: 0; right: 0;
    text-align: center;
    font-size: 12.5px; line-height: 17.5px;
  }
  .page--left .author-note { top: 418px; }
  .page--right .author-note { top: 436px; }
  .author-note strong { font-weight: 700; }
</style>
</head>
<body>
  <main class="spread">
    <section class="page page--left">
      <div class="page-marker" role="img" aria-label="Two wine glasses marking the page number"></div>
      <span class="page-number">1</span>
      <p class="quote">The discovery of a good<br>wine is increasingly better<br>for mankind than the<br>discovery of a new star.<br>– Lorenzo Vantieri</p>
      <p class="author-note"><strong>Lorenzo Vantieri</strong> (1487 –1551)<br>Florentine Vintner, Poet, Cellar Keeper, Traveller,<br>Letter Writer, Garden Designer, Astronomer,<br>Collector of Maps and Old Manuscripts.</p>
    </section>
    <section class="page page--right">
      <div class="page-marker" role="img" aria-label="Two wine glasses marking the page number"></div>
      <span class="page-number">2</span>
      <p class="quote">Be careful to trust a person<br>who does not like wine.<br>– Anselm Rohrbach</p>
      <p class="author-note"><strong>Anselm Rohrbach (1902 –1974)</strong><br>Bavarian Cooper, Essayist, Cellar Master, Travel Writer, Teacher,<br>and Amateur Astronomer.</p>
    </section>
  </main>
</body>
</html>
```